Create Bramble Learning Works a card design that will stick in the mind of prospects.

Bramble Learning Works specialises designs and produces training video, animation, illustration and text.

We need a card design that oozes class and leaves the prospect brimming with confidence.

The design will feature the Bramble Learning Works all black logo (uploaded). The design may also use the shade of orange from the orange version of the logo (uploaded). Note, just the color is to be used e.g. for the back of the card, not the orange logo itself.

The Bramble brand is about authenticity, quality, maturity and assurance. We are a safe buy when it comes to the prospects next project.

Target Market(s)

The primary target is training managers or others who are responsible for choosing to hire companies to produce their training media e.g. video. This will usually be a large spend so they need to have confidence.

Industry/Entity Type

Training

Contact Information for Business Card

FRONT:

Bramble Learning Works
Phone: 03 9512 4379
1st Floor, 418 Ferncliff Road
Mt Dellmoor
VIC 3187
Australia
www.bramblelearning.com.au

Lionel Pratt
Founder and Lead Consultant
mobile: +61 3 0452 736 218
email: lionel@bramblelearning.com.au

BACK:
Specialising in design and production of training:

video
animation
illustration
text

for delivery via internet, intranet and/or LMS.

Number of Pages Required

4 page

Font styles to use
Sans Serif

Requirements
Must have
• The black logo uploaded with the brief.
Nice to have
• The inclusion of the shade of orange found in the orange logo also uploaded with the brief. One example would be having the back of the card in this orange and using a white font for the text. But I want the designer to work this out.
Should not have
• No colours other than black and the orange included in the uploaded orange logo.

```html
<!DOCTYPE html>
<html lang="en">
<head>
<meta charset="utf-8">
<title>Bramble Learning Works – Business Card</title>
<link href="https://fonts.googleapis.com/css2?family=Arimo:wght@400;700&display=swap" rel="stylesheet">
<style>
  :root {
    --card-black: #231f20;
    --brand-orange: #e87722;
    --paper-white: #ffffff;
    --ink-dark: #1e1e1e;
    --faint-mark: #4a4748;
    --stage: #d6d6d6;
  }
  * { margin: 0; padding: 0; box-sizing: border-box; }
  html, body {
    width: 1200px; height: 1200px; overflow: hidden;
    background: var(--stage);
    font-family: "Arimo", Arial, sans-serif;
  }
  .card {
    position: absolute; left: 238px;
    width: 723px; height: 443px;
    background: var(--card-black);
    overflow: hidden;
    box-shadow: 0 14px 24px rgba(0,0,0,0.25);
  }
  .card--front { top: 101px; }
  .card--back { top: 624px; }
  .card__shape { position: absolute; inset: 0; }
  .abs { position: absolute; white-space: nowrap; }

  .person__name { left: 47px; top: 188px; font-size: 22px; font-weight: 700; color: var(--brand-orange); }
  .person__title { left: 47px; top: 213px; font-size: 15.5px; font-weight: 700; color: var(--paper-white); }

  .contact { display: flex; align-items: center; gap: 13px; font-size: 14.5px; }
  .contact__key {
    width: 20px; height: 20px; background: var(--brand-orange);
    color: var(--paper-white); font-weight: 700; font-size: 13px;
    display: flex; align-items: center; justify-content: center;
  }
  .contact--light { color: var(--paper-white); }
  .contact--dark { color: var(--ink-dark); }
  .mobile { left: 46px; top: 264px; }
  .email { left: 46px; top: 285px; }

  .brand-mark { left: 420px; top: 130px; display: flex; align-items: center; gap: 10px; }
  .brand-mark__dot { width: 18px; height: 18px; border-radius: 50%; background: var(--brand-orange); }
  .brand-mark__name { font-size: 40px; font-weight: 700; color: var(--brand-orange); }

  .company__name { left: 372px; top: 302px; font-size: 21px; font-weight: 700; color: var(--ink-dark); }
  .company__address { left: 372px; top: 334px; font-size: 14px; line-height: 17px; color: var(--ink-dark); }
  .phone { left: 372px; top: 375px; }
  .web { left: 372px; top: 396px; }

  .back-mark {
    left: 0; right: 0; top: 105px; text-align: center;
    font-size: 130px; font-weight: 700; color: var(--faint-mark);
  }
  .services { left: 0; right: 0; top: 353px; text-align: center; color: var(--paper-white); font-size: 13.5px; }
  .services__list { margin: 10px 0 9px; color: var(--brand-orange); font-size: 14.5px; }
  .services__list span + span { border-left: 2px solid var(--paper-white); padding-left: 10px; margin-left: 10px; }
</style>
</head>
<body>
  <section class="card card--front">
    <svg class="card__shape" width="723" height="443" viewBox="0 0 723 443">
      <polygon points="366,0 373,0 320,443 313,443" fill="var(--brand-orange)"/>
      <polygon points="373,0 681,0 626,443 320,443" fill="var(--paper-white)"/>
      <polygon points="681,0 688,0 633,443 626,443" fill="var(--brand-orange)"/>
    </svg>

    <div class="abs person__name">Lionel Pratt</div>
    <div class="abs person__title">Founder and Lead Consultant</div>
    <div class="abs contact contact--light mobile"><span class="contact__key">m</span>+61 3 0452 736 218</div>
    <div class="abs contact contact--light email"><span class="contact__key">e</span>lionel@bramblelearning.com.au</div>

    <div class="abs brand-mark"><span class="brand-mark__dot"></span><span class="brand-mark__name">Bramble</span></div>

    <div class="abs company__name">Bramble Learning Works</div>
    <div class="abs company__address">1st Floor, 418 Ferncliff Road<br>Mt Dellmoor, VIC 3187, Australia</div>
    <div class="abs contact contact--dark phone"><span class="contact__key">p</span>03 9512 4379</div>
    <div class="abs contact contact--dark web"><span class="contact__key">w</span>www.bramblelearning.com.au</div>
  </section>

  <section class="card card--back">
    <div class="abs back-mark">Bramble</div>
    <div class="abs services">
      <p>Specialising in design and production of training:</p>
      <p class="services__list"><span>video</span><span>animation</span><span>illustration</span><span>text</span></p>
      <p>for delivery via internet, intranet and/or LMS.</p>
    </div>
  </section>
</body>
</html>
```